Software Review & Lead Gen Website Needs a Design

We are starting a software lead generation company in the Appointment Reminder space. Our business model is very similar to toolcompass.net. We get paid when we introduce a qualified buyer to a software vendor by vetting out each buyer with a phone call with one of our experts.

The site needs to entice the buyer to call us or submit a form on our site for a quick interview where we will then narrow down the field of vendors to 3 that best suit their needs. Everything is 100% free for the buyer. We also provide reviews of each software vendor so that they can compare.

The website can currently be found at nudgeratings.com (this is a mockup we have just been playing around with - we do not prefer this specific design look, although we do like the font style, icons and color styles)

We're looking for a design of the home page and of the review page (for the reviews, we are going to have a medical reviews page, a dental reviews page, vision reviews page and business reviews page - reminder software will vary depending on the category of the organization) about us, for vendors page, and how it works page.

We've attached some really basic mockups we created of each page in a PDF. Each page is labeled (some have a "2" and that just means as you scroll down) You definitely don't have to copy what we have - we've been told that its too "busy" looking. We feel that a professional web designer could do a much better job of simplifying the UI and creating a better flow as well as just making it more pleasing on the eyes.

For inspiration, see toolcompass.net (they have the exact same business model, but they work in multiple industries whereas we just work with reminder software) and pebblework.com (also a slightly similar model).

Feel free to use the text from our mockups, create your own, or just use latin and we can fill in the rest with what fits best in your design.

We have a logo that we can send you, but no photos, so please use your best judgement and we'll make changes as needed.

Most important to us:

- Strong, simple calls to action - we want the buyers to call us directly, download our buyer's guide (in exchange for their email) or fill out a form for us to call them - when we get them on the phone, we conduct a quick interview to assess their needs and then narrow down the vendors to just 3. The vendors then pay us for the introduction to the buyer.

- Conveys to the visitor how we can help them (narrow down their search, allow them to compare vendors, save time and avoid mistakes)

- Narrow down each visitor by the type of company they are (Medical, Dental, Vision or Business)

We like white space, and simple / modern looks.

Target Market(s)

Doctors offices, office managers and business people

Industry/Entity Type

Software

Font styles to use
Sans Serif

Colors
85abd2
33a6d7
33b7a4
f68d4d
f8ba93
aaaaaa
000000
cfcfcf

Requirements
Must have
• See description above
Nice to have
• We like the font ff-tisa-web-pro and can provide if necessary

```html
<!DOCTYPE html>
<html lang="en">
<head>
<meta charset="utf-8">
<title>Nudge Ratings – Appointment Reminder Software Reviews</title>
<link href="https://fonts.googleapis.com/css2?family=Lato:ital,wght@0,300;0,400;0,700;1,400;1,700&display=swap" rel="stylesheet">
<style>
:root{
  --sky:#85abd2;
  --blue:#33a6d7;
  --teal:#33b7a4;
  --orange:#f68d4d;
  --peach:#f8ba93;
  --grey:#aaaaaa;
  --ink:#000000;
  --line:#cfcfcf;
  --text:#555555;
  --soft:#f4f4f4;
  --foot:#ececec;
}
*{box-sizing:border-box;margin:0;padding:0}
html,body{width:1200px;height:2696px;overflow:hidden}
body{font-family:"Lato",Arial,sans-serif;color:var(--text);background:#fff;position:relative;font-size:14px;line-height:1.5}
.wrap{position:absolute;left:72px;width:1056px}
a{color:inherit;text-decoration:none}

/* header */
.site-header{position:absolute;top:0;left:0;width:1200px;height:96px;border-bottom:1px solid #eee}
.brand{position:absolute;left:72px;top:30px;display:flex;align-items:center;gap:10px}
.brand-mark{width:36px;height:36px;background:var(--blue);border-radius:4px}
.brand-name{font-size:30px;font-weight:700;color:#333;letter-spacing:-.5px}
.main-nav{position:absolute;right:72px;top:24px;display:flex}
.main-nav a{display:block;padding:14px 18px;font-size:16px;color:#444}
.main-nav a.active{background:var(--blue);color:#fff}

/* hero */
.hero{top:96px;height:610px}
.hero h1{position:absolute;top:70px;left:0;font-weight:300;font-size:62px;line-height:1.05;color:#222;letter-spacing:-1px}
.hero h1 span{display:block;font-size:31px;letter-spacing:0;margin-top:12px}
.hero-lede{position:absolute;top:236px;left:0;width:470px;font-size:17px;line-height:1.55;color:#444}
.hero-visual{position:absolute;left:560px;top:40px;width:480px;height:370px;border-radius:8px;background:linear-gradient(160deg,#e8eef4,#c9d4de 60%,#aab6c2)}
.callout{position:absolute;left:252px;top:442px;width:560px;height:136px;background:var(--peach);padding:22px 28px}
.callout p{font-size:15px;color:#333;width:300px;line-height:1.4}
.callout strong{display:block;font-size:22px;font-weight:700;color:#222;margin-top:6px}
.callout .btn{position:absolute;right:28px;top:44px}
.btn{display:inline-block;padding:12px 22px;font-size:15px;font-weight:700;color:#fff;text-align:center}
.btn-orange{background:var(--orange)}
.btn-blue{background:var(--blue)}

/* categories */
.categories{top:730px;height:280px;border-top:1px solid #eee;padding-top:28px}
.section-title{font-size:32px;font-weight:400;color:var(--blue);text-align:center}
.section-sub{font-size:15px;color:#333;text-align:center;margin-top:4px}
.tiles{display:flex;gap:24px;margin-top:24px}
.tile{flex:1;height:168px;color:#fff;display:flex;flex-direction:column;align-items:center;justify-content:flex-end;padding-bottom:18px}
.tile svg{margin-bottom:10px}
.tile span{font-size:34px;font-weight:400}
.tile-dental{background:var(--blue)}
.tile-medical{background:var(--teal)}
.tile-vision{background:var(--orange)}
.tile-business{background:var(--sky)}

/* testimonials */
.testimonials{top:1052px;height:300px}
.block-title{font-size:22px;color:var(--blue);font-weight:400;padding-bottom:10px;border-bottom:1px solid var(--line)}
.quote-card{margin-top:18px;border:1px solid var(--line);height:200px;position:relative;padding:30px 30px 30px 190px}
.quote-photo{position:absolute;left:34px;top:30px;width:128px;height:128px;border-radius:50%;background:linear-gradient(150deg,#c9ccd0,#8d949b)}
.quote-card blockquote{font-style:italic;font-weight:700;font-size:16px;color:#222}
.quote-card p{font-size:14px;margin-top:8px;color:#555}
.quote-by{position:absolute;left:190px;bottom:14px;font-size:14px}
.quote-by b{color:var(--blue);margin-right:6px}
.pager{position:absolute;right:0;bottom:-28px;display:flex;gap:4px}
.pager i{display:block;width:18px;height:18px;background:#666}
.pager i+i{background:var(--blue)}

/* vendors */
.vendors{top:1378px;height:270px;display:flex;gap:24px}
.vendor{flex:1}
.vendor-img{height:206px;position:relative;display:flex;align-items:center;justify-content:center;color:#fff;font-size:22px}
.v1{background:linear-gradient(150deg,#3c4a55,#1d2830)}
.v2{background:linear-gradient(150deg,#2d5a73,#15303f)}
.v3{background:linear-gradient(150deg,#4d5d6c,#222c36)}
.vendor-img span{position:relative}
.vendor-actions{display:flex;margin-top:12px;justify-content:space-between}
.vendor-actions .btn{width:132px;padding:10px 0;font-size:14px;font-weight:400}

/* lower */
.lower-main{position:absolute;left:72px;top:1666px;width:720px}
.intro-copy p{font-size:14px;line-height:1.45;margin-bottom:8px;color:#555}
.lead-form{margin-top:16px;background:var(--soft);border:1px solid var(--line);height:494px;padding:24px 28px;position:relative}
.lead-form h3{font-size:24px;font-weight:400;color:var(--blue);line-height:1.25}
.form-note{position:absolute;left:28px;top:120px;width:270px;font-size:13px;color:#555}
.form-note p{margin-bottom:14px}
.fields{position:absolute;left:330px;top:104px;width:300px}
.field{height:36px;border:1px solid var(--line);background:#fff;margin-bottom:10px;padding:8px 12px;font-size:13px;color:var(--grey);position:relative}
.field.select::after{content:"";position:absolute;right:12px;top:14px;border:5px solid transparent;border-top-color:#666}
.fine-print{position:absolute;left:28px;bottom:26px;width:270px;font-size:12px;color:#777}
.lead-form .btn{position:absolute;left:330px;bottom:26px;width:300px;font-size:18px}

.lower-side{position:absolute;left:824px;top:1666px;width:304px}
.side-title{font-size:22px;font-weight:400;padding-bottom:6px;border-bottom:1px solid var(--line)}
.side-title.orange{color:var(--orange)}
.side-title.blue{color:var(--blue)}
.guide-name{color:var(--blue);font-size:15px;margin-top:10px}
.guide-desc{font-size:13px;color:#555}
.guide-cover{margin:14px auto 0;width:170px;height:150px;background:linear-gradient(150deg,#dfe6ec,#9fb0c0)}
.lower-side .btn{display:block;margin-top:14px;font-size:16px}
.report{margin-top:26px}
.report-item{display:flex;gap:12px;padding:12px 0;border-bottom:1px solid #eee}
.report-thumb{width:64px;height:56px;flex:none;background:linear-gradient(150deg,#7fa6c4,#3e6580)}
.report-item h4{font-size:14px;color:var(--blue);font-weight:700;line-height:1.3}
.report-item p{font-size:12px;color:#777;line-height:1.35}

/* footer */
.site-footer{position:absolute;left:0;top:2372px;width:1200px;height:324px;background:var(--foot);border-top:1px solid var(--line)}
.foot-cols{position:absolute;left:72px;top:34px;width:1056px;display:flex;gap:40px}
.foot-col{flex:1}
.foot-col h5{font-size:18px;font-weight:400;color:var(--blue);margin-bottom:10px}
.foot-col li{list-style:none;font-size:13px;color:#555;line-height:1.9}
.foot-col li::before{content:"›";color:var(--blue);margin-right:6px}
.socials{display:flex;gap:8px}
.socials i{width:30px;height:30px;border-radius:50%;background:var(--blue);display:block}
.foot-address{font-size:13px;line-height:1.7}
.copyright{position:absolute;left:72px;top:110px;font-size:13px;color:#555}
</style>
</head>
<body>

<header class="site-header">
  <a class="brand" href="#"><span class="brand-mark"></span><span class="brand-name">nudge ratings</span></a>
  <nav class="main-nav">
    <a class="active" href="#">Home</a><a href="#">About Us</a><a href="#">Reviews</a><a href="#">Blog</a><a href="#">Contact Us</a>
  </nav>
</header>

<section class="wrap hero">
  <h1>The Authority on<span>Appointment Reminder Software</span></h1>
  <p class="hero-lede">Nudge Ratings connects Buyers with the software services that match their needs. Compare in-depth vendor reviews, seepricing &amp; demos and make the best selection for</p>
  <div class="hero-visual" role="img" aria-label="Desktop monitor showing the reviews website"></div>
  <div class="callout">
    <p>We'll help determine which patient reminder services is best for you<strong>Call us at 555 -555 -5555</strong></p>
    <a class="btn btn-orange" href="#">Free Consultation</a>
  </div>
</section>

<section class="wrap categories">
  <h2 class="section-title">Compare Reviews by Category</h2>
  <p class="section-sub">Select a Category to See Reviews</p>
  <div class="tiles">
    <a class="tile tile-dental" href="#">
      <svg width="54" height="58" viewBox="0 0 54 58" fill="#fff"><path d="M27 8c-6-6-20-6-22 6-2 10 4 16 6 26 2 9 4 16 8 16 4 0 4-12 8-12s4 12 8 12c4 0 6-7 8-16 2-10 8-16 6-26-2-12-16-12-22-6z"/></svg>
      <span>Dental</span></a>
    <a class="tile tile-medical" href="#">
      <svg width="56" height="56" viewBox="0 0 56 56" fill="#fff"><path d="M20 2h16v18h18v16H36v18H20V36H2V20h18z"/></svg>
      <span>Medical</span></a>
    <a class="tile tile-vision" href="#">
      <svg width="70" height="44" viewBox="0 0 70 44"><path d="M2 22C14 4 56 4 68 22 56 40 14 40 2 22z" fill="#fff"/><circle cx="35" cy="22" r="12" fill="var(--orange)"/><circle cx="35" cy="22" r="6" fill="#fff"/></svg>
      <span>Vision</span></a>
    <a class="tile tile-business" href="#">
      <svg width="62" height="52" viewBox="0 0 62 52" fill="#fff"><path d="M22 2h18a4 4 0 0 1 4 4v6h14a4 4 0 0 1 4 4v32a4 4 0 0 1-4 4H4a4 4 0 0 1-4-4V16a4 4 0 0 1 4-4h14V6a4 4 0 0 1 4-4zm2 6v4h14V8z"/></svg>
      <span>Businesss</span></a>
  </div>
</section>

<section class="wrap testimonials">
  <h2 class="block-title">What Say Our Clients About Us</h2>
  <div class="quote-card">
    <div class="quote-photo" role="img" aria-label="Portrait of a smiling dentist"></div>
    <blockquote>Nudge Ratings saved me so much time researching software, and the best part is they did it for free!</blockquote>
    <p>Lorem ipsum dolor sit amet, consectetur adipiscing elit. Curabitur mollis lectus at odio egestas, quis placerat libero facilisis. Proin sollicitudin felis a dapibus sagittis. Morbi mattis nulla nec lacus faucibus, vitae tincidunt justo suscipit. Integer lobortis.</p>
    <div class="quote-by"><b>Bill,</b>Preferred Dentist</div>
    <div class="pager"><i></i><i></i></div>
  </div>
</section>

<section class="wrap vendors">
  <div class="vendor">
    <div class="vendor-img v1" role="img" aria-label="Office workspace photo"><span>Vendor 1 Snippet Review</span></div>
    <div class="vendor-actions"><a class="btn btn-blue" href="#">In Depth Analysis</a><a class="btn btn-orange" href="#">User Reviews</a></div>
  </div>
  <div class="vendor">
    <div class="vendor-img v2" role="img" aria-label="Business team at work photo"><span>Vendor 2 Snippet Review</span></div>
    <div class="vendor-actions"><a class="btn btn-blue" href="#">In Depth Analysis</a><a class="btn btn-orange" href="#">User Reviews</a></div>
  </div>
  <div class="vendor">
    <div class="vendor-img v3" role="img" aria-label="Medical office photo"><span>Vendor 3 Snippet Review</span></div>
    <div class="vendor-actions"><a class="btn btn-blue" href="#">In Depth Analysis</a><a class="btn btn-orange" href="#">User Reviews</a></div>
  </div>
</section>

<section class="lower-main">
  <div class="intro-copy">
    <p>Appointment Reminder and Customer Engagement Software with growth as businesses of all kinds are realizing how important it is to reduce appointment cancellations and improve how they interact with their valuable customer &amp; patient bases.</p>
    <p>As these Businesses evaluate which options available to them are best fit it can become a daunting task to sift through each vendor's website, reach out individually to see presentations and compare pricing.</p>
    <p>Nudge Ratings is a 100% Free Service to help buyers find the best vendors that match their needs, save time and avoid costly mistakes. We are completely free for buyers.</p>
  </div>
  <form class="lead-form">
    <h3>Get Introduced to the Top-Rated Reminder services in Seconds</h3>
    <div class="form-note">
      <p>"Just tell us a few basic details about your organization and we'll match you with the best of the best"</p>
      <p>Get Price Quotes, Product Demos, Our Free Buyer Guide without the hassle of tracking down each vendor yourself</p>
    </div>
    <div class="fields">
      <div class="field">Your Company Name</div>
      <div class="field">First Name</div>
      <div class="field">Last Name</div>
      <div class="field">Email</div>
      <div class="field">Phone</div>
      <div class="field select">Organization Type</div>
      <div class="field select">State</div>
    </div>
    <p class="fine-print">By clicking the button to the right you have read and agree to our Terms of use and privacy Policy</p>
    <a class="btn btn-orange" href="#">Show Me The Money !</a>
  </form>
</section>

<aside class="lower-side">
  <h3 class="side-title orange">Free PDF Guide</h3>
  <p class="guide-name">Ultimate Reminder Services Buyers' Guide</p>
  <p class="guide-desc">The Definitive Guide To Buying the Perfect Reminder Software for your Organization</p>
  <div class="guide-cover" role="img" aria-label="Cover of the buyer's guide booklet"></div>
  <a class="btn btn-orange" href="#">GET BUYER'S GUIDE</a>
  <div class="report">
    <h3 class="side-title blue">Reminder Report</h3>
    <div class="report-item"><div class="report-thumb" role="img" aria-label="Article thumbnail"></div><div><h4>Top 5 HIPAA Questions Answered</h4><p>Learn what you need to know before you buy a reminder system.</p></div></div>
    <div class="report-item"><div class="report-thumb" role="img" aria-label="Article thumbnail"></div><div><h4>The Future Of Patient Engagement</h4><p>Simple ways to keep patients coming back on time.</p></div></div>
    <div class="report-item"><div class="report-thumb" role="img" aria-label="Article thumbnail"></div><div><h4>Missed appointments add up</h4><p>See what no-shows really cost a small practice.</p></div></div>
  </div>
</aside>

<footer class="site-footer">
  <div class="foot-cols">
    <div class="foot-col">
      <h5>Get in touch</h5>
      <div class="socials"><i></i><i></i><i></i><i></i></div>
    </div>
    <div class="foot-col">
      <h5>Who We Are</h5>
      <ul><li>Home</li><li>About Us</li><li>Reviews</li><li>Blog</li><li>Contact Us</li></ul>
    </div>
    <div class="foot-col">
      <h5>For Vendors</h5>
      <ul><li>Vendor Sign Up</li><li>How it Works</li><li>Buyer Guide</li><li>New Site Scale</li><li>Lets Connect</li></ul>
    </div>
    <div class="foot-col">
      <h5>For Buyers</h5>
      <ul><li>Medical</li><li>Dental</li><li>Vision</li><li>Business</li><li>Buyers Guide</li></ul>
    </div>
    <div class="foot-col">
      <h5>Our Address</h5>
      <p class="foot-address">48 Larkspur Row,<br>Millbrook Avenue,<br>Northvale<br>555-555-5555<br>info@nudgeratings.com</p>
    </div>
  </div>
  <p class="copyright">© 2014 Nudge Ratings<br>All rights reserved</p>
</footer>

</body>
</html>
```